Book Cover Design Project

I need a book cover design with the title

"Gilded Ledger - A Probe into Avarice and Graft in Australia’s $1 Trillion Retirement Savings Sector"

With a question on the cover of "How much of your superannuation has been stolen? Read this Book to Find Out"

The design should have money and greed based theme such as "$" for "S" in "Super"

Target Market(s)

Members of Superannuation (Pension) funds

Industry/Entity Type

Industry

Requirements
Must have
• Must have a money and greed theme

```html
<!DOCTYPE html>
<html lang="en">
<head>
<meta charset="utf-8">
<title>Gilded Ledger — Book Cover</title>
<link rel="stylesheet" href="https://fonts.googleapis.com/css2?family=Bebas+Neue&display=swap">
<style>
  :root {
    --page-bg: #e4e4e4;
    --cover-bg: #ffffff;
    --ink: #111111;
    --money-red: #d0121b;
    --band-red: #c8101a;
    --band-text: #ffffff;
    --photo-dark: #2a2a2c;
    --photo-mid: #6b6560;
    --photo-light: #d9d4cf;
  }
  * { box-sizing: border-box; margin: 0; padding: 0; }
  html, body {
    width: 1200px; height: 801px; overflow: hidden;
    background: var(--page-bg);
  }
  .book-cover {
    position: absolute;
    left: 380px; top: 36px;
    width: 440px; height: 706px;
    background: var(--cover-bg);
    overflow: hidden;
    font-family: "Bebas Neue", "Arial Narrow", sans-serif;
    color: var(--ink);
  }
  .cover-photo {
    position: absolute;
    left: 0; top: 40px;
    width: 140px; height: 610px;
    background: linear-gradient(180deg, var(--photo-mid) 0%, var(--photo-light) 16%, var(--photo-dark) 38%, var(--photo-dark) 86%, var(--photo-mid) 100%);
    border-radius: 0 40px 20px 0;
  }
  .title-block {
    position: absolute;
    left: 152px; right: 12px; top: 24px;
    text-align: right;
    line-height: 0.92;
    font-weight: 400;
    white-space: nowrap;
  }
  .title-block span { display: block; }
  .title-main { font-size: 62px; color: var(--money-red); }
  .title-small { font-size: 28px; }
  .title-mid { font-size: 44px; }
  .title-figure { font-size: 52px; color: var(--money-red); }
  .title-large { font-size: 72px; }
  .title-tail { font-size: 26px; }
  .rule {
    position: absolute;
    right: 12px; top: 412px;
    width: 250px; height: 3px;
    background: var(--money-red);
  }
  .teaser {
    position: absolute;
    right: 12px; top: 424px;
    width: 250px;
    text-align: center;
    line-height: 0.95;
  }
  .teaser-question { font-size: 24px; }
  .teaser-call { font-size: 28px; color: var(--money-red); }
  .author-band {
    position: absolute;
    left: 4px; right: 4px; top: 660px;
    height: 40px;
    background: var(--band-red);
    color: var(--band-text);
    font-size: 30px;
    letter-spacing: 6px;
    display: flex; align-items: center; justify-content: center;
    padding-top: 3px;
  }
</style>
</head>
<body>
  <main class="book-cover">
    <div class="cover-photo" role="img" aria-label="Photo of a flashy businessman in tinted glasses and gold chains holding a banknote and a cigar"></div>

    <h1 class="title-block">
      <span class="title-main">Gilded</span>
      <span class="title-main">Ledger</span>
      <span class="title-small">-A Probe into</span>
      <span class="title-mid">Avarice and</span>
      <span class="title-mid">Graft in</span>
      <span class="title-small">Australia’s</span>
      <span class="title-figure">$1 Trillion</span>
      <span class="title-large">Retirement</span>
      <span class="title-tail">Savings Sector</span>
    </h1>

    <div class="rule"></div>

    <p class="teaser">
      <span class="teaser-question">How much of<br>your superannuation<br>has been stolen?</span><br>
      <span class="teaser-call">Read this book<br>to find out!</span>
    </p>

    <div class="author-band">Author Name</div>
  </main>
</body>
</html>
```